Corvelle Matchmaking - Innovative AI-based Online Dating App

Hello, I am creating a new online dating app that subsumes the personalization and compatibility analysis of human matchmaking, but is combined with the convenience of modern dating apps such as brisket. The app is called Corvelle.

There is a lot of pain and fatigue in modern online dating. Corvelle uses a concise but effective questionnaire that is combined with cutting-edge AI, social psychology research, and psycholinguistic modelling to effectively and conveniently find dating matches with real compatibility - as opposed to any major app on the market. A personalized introduction for every user is generated everyday to introduce you to a new potential match - this introduction is totally unique and will never be seen before or again. The introduction is intertwined with the user’s images to create an attractive “newsletter” feel.

"Corvelle" is Italian for lagoon, which is "a shallow body of water protected from a larger body of water (usually the ocean) by sandbars, barrier islands, or coral reefs." Lagoons are beautiful, tropical, lush watery paradises - as I see it. This is meant to be the inspiration for the feel, color scheme and design of the app.

To that end, I have included concept images of lagoons to evoke the feeling of a paradise getaway where one may meet their soulmate. This is the feeling I would like to convey with the minimalist app design this product needs to compete.

I have included screenshots of the current app UI. There is a screen for
1) potential matches and incoming likes (just like Brisket) with a logo at the top. There are “Like”, “Dislike”, “Super Like”, and “Super Dislike” buttons that float over the screen as it scrolls. These button shape/colors likely need to change to match the rest of the design
2) Overview of message threads with each match
3) View of message threads
4) Settings page

I would like
1) the logo/header image to be redone (as well as the like/dislike/super like/super dislike buttons to be redone to match the new design)
2) icons for the 4 pages in the bottom navigation bar to be redone
3) color scheme to be optimized and evoking of the desired paradise but professional feeling of a hyper-intelligent (but also empathetic) matchmaker
4) design for the settings screen (to look professional and competitive with other dating apps)

The color scheme /layout/spacing/font(s) for the bubbles on the screen where new potential matches are introduced is the most important part of the design I’m looking for. It’s currently a stack of rounded rectangles basically, but I’m open to all ideas to make this app look as professional as possible while conveying the desired elegance, empathy, and uniqueness of the brand.

Thank you!

Target Market(s)

Single men and women ages 20 - 45

Industry/Entity Type

Online dating / Matchmaking

Requirements
Must have
• For the main screen where new users are being introduced (i.e. the "swipe" page on most dating apps) - some amount of matchmaking introductory text MUST be shown above the user's first profile picture, as indicated in the current screenshots.
Nice to have
• Re-designs of the top "Corvelle" logo/emblem would be nice. If changing the logo, some emblem or graphic in addition to just the text of "Corvelle" would be nice. (Like the way "plumway" has its red flame emblem)
Should not have
• The main "swipe" page should not look identical to other dating apps in the sense of being >90% just a user's first dating profile image. The competitive edge to this app is the user-to-user specific matchmaking introductory text, so some of that must be visible before a user scrolls down for further profile information.

```html
<!DOCTYPE html>
<html lang="en">
<head>
<meta charset="utf-8">
<title>Corvelle – App Screens</title>
<link rel="stylesheet" href="https://fonts.googleapis.com/css2?family=Quicksand:wght@400;500;600;700&display=swap">
<style>
  :root {
    --canvas: #e3e8f0;
    --phone: #ffffff;
    --teal: #1cc3b8;
    --mint: #c8fbf3;
    --ink: #111418;
    --intro-ink: #1f4b4b;
    --muted: #6b7480;
    --panel: #eef2f7;
    --line: #d6dde6;
    --button-glass: rgba(128, 138, 150, 0.72);
    --verify: #2f7be5;
  }
  * { box-sizing: border-box; margin: 0; padding: 0; }
  html, body { width: 1200px; height: 1200px; overflow: hidden; background: var(--canvas); }
  body { font-family: "Quicksand", sans-serif; color: var(--ink); }
  .stage { position: relative; width: 1000px; height: 1000px; transform: scale(1.2); transform-origin: 0 0; }
  .phone { position: absolute; width: 390px; height: 843px; background: var(--phone); border-radius: 30px; overflow: hidden; }
  .phone--match { left: 80px; top: 55px; }
  .phone--settings { left: 530px; top: 101px; }
  .abs { position: absolute; }
  .status-time { left: 24px; top: 13px; width: 56px; text-align: center; font-size: 15px; font-weight: 700; }
  .status-icons { right: 20px; top: 16px; }
  .wordmark { left: 15px; font-size: 29px; font-weight: 600; color: var(--teal); letter-spacing: -0.3px; line-height: 1; }
  .header-icon { transform: translate(-50%, -50%); }
  .intro-card { left: 16px; top: 122px; width: 358px; height: 211px; background: var(--mint); border-radius: 16px; padding: 16px 14px 0 16px; font-size: 13.6px; line-height: 18px; color: var(--intro-ink); font-weight: 500; }
  .intro-card b { font-weight: 700; }
  .profile-photo { left: 16px; top: 350px; width: 358px; height: 412px; border-radius: 18px; overflow: hidden;
    background: radial-gradient(ellipse at 55% 55%, #4a5a34 0%, #2f3a24 45%, #1d2418 100%); }
  .profile-name { left: 16px; top: 273px; color: #fff; font-size: 21px; font-weight: 600; }
  .action { width: 58px; height: 58px; border-radius: 50%; background: var(--button-glass); display: flex; align-items: center; justify-content: center; transform: translate(-50%, -50%); }
  .action--big { width: 80px; height: 80px; }
  .nav-icon { transform: translate(-50%, -50%); }
  .home-indicator { left: 125px; width: 139px; height: 4px; border-radius: 2px; background: var(--ink); }
  .profile-card { left: 16px; top: 123px; width: 358px; height: 207px; background: var(--panel); border-radius: 18px; }
  .avatar { left: 16px; top: 16px; width: 100px; height: 100px; border-radius: 50%; background: linear-gradient(160deg, #2aa6e8 0%, #1a86d0 55%, #5a3c2c 100%); }
  .avatar-edit { left: 71px; top: 97px; width: 26px; height: 26px; border-radius: 50%; background: var(--teal); border: 2px solid #fff; display: flex; align-items: center; justify-content: center; }
  .profile-name-lg { left: 132px; top: 46px; font-size: 18px; font-weight: 600; }
  .verify { left: 132px; top: 70px; display: flex; align-items: center; gap: 5px; font-size: 12px; color: var(--muted); font-weight: 500; }
  .stat { width: 140px; text-align: center; transform: translateX(-50%); }
  .stat-value { font-size: 28px; font-weight: 700; line-height: 1; }
  .stat-label { margin-top: 14px; font-size: 12px; color: var(--muted); font-weight: 500; }
  .stat-divider { left: 179px; top: 143px; width: 1px; height: 38px; background: var(--line); }
  .section-title { left: 16px; font-size: 16px; font-weight: 600; }
  .settings-card { left: 16px; width: 358px; background: var(--panel); border-radius: 18px; }
  .row-label { left: 16px; font-size: 14px; font-weight: 600; transform: translateY(-50%); }
  .row-value { right: 16px; font-size: 13px; color: var(--muted); font-weight: 500; transform: translateY(-50%); display: flex; align-items: center; gap: 8px; }
  .separator { left: 16px; right: 16px; height: 1px; background: var(--line); }
  .slider-track { left: 16px; right: 16px; height: 2px; background: var(--line); }
  .slider-fill { height: 2px; background: var(--teal); }
  .knob { width: 24px; height: 24px; border-radius: 50%; background: #fff; box-shadow: 0 1px 4px rgba(0,0,0,.22); transform: translate(-50%, -50%); }
  .toggle { right: 16px; width: 48px; height: 24px; border-radius: 12px; background: var(--teal); transform: translateY(-50%); }
  .toggle::after { content: ""; position: absolute; right: 1px; top: 1px; width: 22px; height: 22px; border-radius: 50%; background: #fff; box-shadow: 0 1px 3px rgba(0,0,0,.2); }
  .nav-bar { left: 0; top: 763px; width: 390px; height: 80px; background: #fff; }
</style>
</head>
<body>
<div class="stage">

  <!-- Match introduction screen -->
  <section class="phone phone--match">
    <div class="abs status-time">9:41</div>
    <svg class="abs status-icons" width="68" height="12" viewBox="0 0 68 12">
      <rect x="0" y="8" width="3" height="4" rx="1" fill="#111"/><rect x="5" y="6" width="3" height="6" rx="1" fill="#111"/><rect x="10" y="3" width="3" height="9" rx="1" fill="#111"/><rect x="15" y="0" width="3" height="12" rx="1" fill="#111"/>
      <path d="M24 4.5a10 10 0 0 1 14 0l-1.6 1.6a7.7 7.7 0 0 0-10.8 0z M27 7.5a5.5 5.5 0 0 1 8 0L31 11.5z" fill="#111"/>
      <rect x="44" y="1" width="20" height="10" rx="3" fill="none" stroke="#111" stroke-width="1.2"/><rect x="46" y="3" width="16" height="6" rx="1.5" fill="#111"/><rect x="65" y="4" width="2" height="4" rx="1" fill="#111"/>
    </svg>

    <div class="abs wordmark" style="top:60px">corvelle</div>
    <svg class="abs header-icon" style="left:323px;top:75px" width="24" height="24" viewBox="0 0 24 24" fill="none" stroke="#111" stroke-width="1.8" stroke-linecap="round" stroke-linejoin="round">
      <path d="M6 16V11a6 6 0 0 1 12 0v5l1.5 2h-15z"/><path d="M10 21h4"/>
    </svg>
    <svg class="abs header-icon" style="left:362px;top:75px" width="24" height="24" viewBox="0 0 24 24" fill="none" stroke="#111" stroke-width="1.8" stroke-linecap="round">
      <path d="M3 8h10"/><circle cx="17" cy="8" r="3"/><path d="M21 16H11"/><circle cx="7" cy="16" r="3"/>
    </svg>

    <div class="abs intro-card">
      Dear Brandon,<br>
      Allow me to introduce you <b>Natasha</b>, a captivating woman who possesses an enchanting blend of qualities that perfectly align with what you seek in a partner. Her shared interest in creativity is just the beginning of the profound connection you could share. Natsha’s passion for games, documentaries, music and&nbsp; writing mirrors your own, promising endless hours of intellectual simulation and shared experiences.
    </div>

    <div class="abs profile-photo" role="img" aria-label="Profile photo of Natasha in a beanie and fur coat, green-lit night setting">
      <div class="abs profile-name">Natasha, 24</div>
      <div class="abs action" style="left:46px;top:357px">
        <svg width="26" height="26" viewBox="0 0 24 24"><path d="M3 4h4v10H3z M9 4h8.5a2 2 0 0 1 2 1.6l1.4 7a2 2 0 0 1-2 2.4H14l.8 4a1.8 1.8 0 0 1-3.3 1.3L9 15z" fill="#f08a24"/></svg>
      </div>
      <div class="abs action action--big" style="left:131px;top:357px">
        <svg width="28" height="28" viewBox="0 0 24 24" stroke="#f2453d" stroke-width="2.6" stroke-linecap="round"><path d="M4 4l16 16M20 4L4 20"/></svg>
      </div>
      <div class="abs action action--big" style="left:227px;top:357px">
        <svg width="36" height="36" viewBox="0 0 24 24"><path d="M12 21s-8-5.2-8-11a4.5 4.5 0 0 1 8-2.8A4.5 4.5 0 0 1 20 10c0 5.8-8 11-8 11z" fill="#17dccd"/></svg>
      </div>
      <div class="abs action" style="left:312px;top:357px">
        <svg width="28" height="28" viewBox="0 0 24 24"><path d="M12 2.5l2.9 6.1 6.6.8-4.9 4.6 1.3 6.6L12 17.3l-5.9 3.3 1.3-6.6-4.9-4.6 6.6-.8z" fill="#2e6fe0"/></svg>
      </div>
    </div>

    <svg class="abs nav-icon" style="left:61px;top:790px" width="28" height="28" viewBox="0 0 28 28" fill="none" stroke="#5d6773" stroke-width="1.8"><rect x="3" y="3" width="9" height="9" rx="2"/><rect x="16" y="3" width="9" height="9" rx="2"/><rect x="3" y="16" width="9" height="9" rx="2"/><rect x="16" y="16" width="9" height="9" rx="2"/></svg>
    <svg class="abs nav-icon" style="left:150px;top:790px" width="30" height="30" viewBox="0 0 24 24"><path d="M12 21s-8-5.2-8-11a4.5 4.5 0 0 1 8-2.8A4.5 4.5 0 0 1 20 10c0 5.8-8 11-8 11z" fill="var(--teal)"/></svg>
    <svg class="abs nav-icon" style="left:239px;top:790px" width="30" height="30" viewBox="0 0 28 28" fill="none" stroke="#5d6773" stroke-width="1.8" stroke-linejoin="round"><path d="M4 5h20v15H12l-5 4v-4H4z"/><path d="M14 17s-4-2.6-4-5.3a2.2 2.2 0 0 1 4-1.3 2.2 2.2 0 0 1 4 1.3c0 2.7-4 5.3-4 5.3z"/></svg>
    <svg class="abs nav-icon" style="left:329px;top:790px" width="30" height="30" viewBox="0 0 24 24" fill="none" stroke="#5d6773" stroke-width="1.6" stroke-linejoin="round"><circle cx="12" cy="12" r="3"/><path d="M10.3 3h3.4l.5 2.4 1.8.8 2.1-1.3 2.4 2.4-1.3 2.1.8 1.8 2.4.5v3.4l-2.4.5-.8 1.8 1.3 2.1-2.4 2.4-2.1-1.3-1.8.8-.5 2.4h-3.4l-.5-2.4-1.8-.8-2.1 1.3-2.4-2.4 1.3-2.1-.8-1.8L2.6 13.7v-3.4l2.4-.5.8-1.8-1.3-2.1 2.4-2.4 2.1 1.3 1.8-.8z"/></svg>
    <div class="abs home-indicator" style="top:829px"></div>
  </section>

  <!-- Settings screen -->
  <section class="phone phone--settings">
    <div class="abs status-time">9:41</div>
    <svg class="abs status-icons" width="68" height="12" viewBox="0 0 68 12">
      <rect x="0" y="8" width="3" height="4" rx="1" fill="#111"/><rect x="5" y="6" width="3" height="6" rx="1" fill="#111"/><rect x="10" y="3" width="3" height="9" rx="1" fill="#111"/><rect x="15" y="0" width="3" height="12" rx="1" fill="#111"/>
      <path d="M24 4.5a10 10 0 0 1 14 0l-1.6 1.6a7.7 7.7 0 0 0-10.8 0z M27 7.5a5.5 5.5 0 0 1 8 0L31 11.5z" fill="#111"/>
      <rect x="44" y="1" width="20" height="10" rx="3" fill="none" stroke="#111" stroke-width="1.2"/><rect x="46" y="3" width="16" height="6" rx="1.5" fill="#111"/><rect x="65" y="4" width="2" height="4" rx="1" fill="#111"/>
    </svg>

    <div class="abs wordmark" style="top:61px">corvelle</div>

    <div class="abs profile-card">
      <div class="abs avatar" role="img" aria-label="Profile photo of Brandon against a blue sky"></div>
      <div class="abs avatar-edit">
        <svg width="12" height="12" viewBox="0 0 12 12" stroke="#fff" stroke-width="1.6" stroke-linecap="round"><path d="M2.5 9.5l6-6"/><path d="M2 11h8"/></svg>
      </div>
      <div class="abs profile-name-lg">Brandon</div>
      <div class="abs verify">
        <svg width="15" height="15" viewBox="0 0 24 24"><path d="M12 1.5l2.6 2 3.3-.3 1 3.1 2.8 1.8-1 3.1 1 3.1-2.8 1.8-1 3.1-3.3-.3-2.6 2-2.6-2-3.3.3-1-3.1-2.8-1.8 1-3.1-1-3.1 2.8-1.8 1-3.1 3.3.3z" fill="var(--verify)"/><path d="M8 12.2l2.7 2.7L16.2 9.4" fill="none" stroke="#fff" stroke-width="2" stroke-linecap="round" stroke-linejoin="round"/></svg>
        Not verified
      </div>
      <div class="abs stat" style="left:89px;top:140px"><div class="stat-value">87</div><div class="stat-label">Likes me</div></div>
      <div class="abs stat-divider"></div>
      <div class="abs stat" style="left:269px;top:140px"><div class="stat-value">99+</div><div class="stat-label">My Likes</div></div>
    </div>

    <div class="abs section-title" style="top:355px">Discovery Settings</div>
    <div class="abs settings-card" style="top:390px;height:259px">
      <div class="abs row-label" style="top:25px">Distance</div>
      <div class="abs row-value" style="top:25px">5 km</div>
      <div class="abs slider-track" style="top:49px"><div class="slider-fill" style="width:41px"></div></div>
      <div class="abs knob" style="left:57px;top:50px"></div>

      <div class="abs row-label" style="top:96px">Expand search area</div>
      <div class="abs toggle" style="top:96px"></div>
      <div class="abs separator" style="top:124px"></div>

      <div class="abs row-label" style="top:150px">Show Me</div>
      <div class="abs row-value" style="top:150px">Women
        <svg width="8" height="12" viewBox="0 0 8 12" fill="none" stroke="#6b7480" stroke-width="1.6" stroke-linecap="round"><path d="M2 2l4 4-4 4"/></svg>
      </div>
      <div class="abs separator" style="top:175px"></div>

      <div class="abs row-label" style="top:201px">Age</div>
      <div class="abs row-value" style="top:201px">22-27</div>
      <div class="abs slider-track" style="top:226px"><div class="slider-fill" style="margin-left:18px;width:82px"></div></div>
      <div class="abs knob" style="left:34px;top:227px"></div>
      <div class="abs knob" style="left:116px;top:227px"></div>
    </div>

    <div class="abs section-title" style="top:674px">App Settings</div>
    <div class="abs settings-card" style="top:710px;height:120px">
      <div class="abs row-label" style="top:28px">Privacy Policy</div>
      <svg class="abs" style="right:22px;top:21px" width="9" height="14" viewBox="0 0 9 14" fill="none" stroke="#111" stroke-width="1.8" stroke-linecap="round"><path d="M2 2l5 5-5 5"/></svg>
      <div class="abs separator" style="top:48px"></div>
    </div>

    <div class="abs nav-bar">
      <svg class="abs nav-icon" style="left:61px;top:27px" width="28" height="28" viewBox="0 0 28 28" fill="none" stroke="#5d6773" stroke-width="1.8"><rect x="3" y="3" width="9" height="9" rx="2"/><rect x="16" y="3" width="9" height="9" rx="2"/><rect x="3" y="16" width="9" height="9" rx="2"/><rect x="16" y="16" width="9" height="9" rx="2"/></svg>
      <svg class="abs nav-icon" style="left:150px;top:27px" width="30" height="30" viewBox="0 0 24 24" fill="none" stroke="#5d6773" stroke-width="1.6" stroke-linejoin="round"><path d="M12 20s-8-5-8-10.6a4.4 4.4 0 0 1 8-2.6 4.4 4.4 0 0 1 8 2.6C20 15 12 20 12 20z"/></svg>
      <svg class="abs nav-icon" style="left:239px;top:27px" width="30" height="30" viewBox="0 0 28 28" fill="none" stroke="#5d6773" stroke-width="1.8" stroke-linejoin="round"><path d="M4 5h20v15H12l-5 4v-4H4z"/><path d="M14 17s-4-2.6-4-5.3a2.2 2.2 0 0 1 4-1.3 2.2 2.2 0 0 1 4 1.3c0 2.7-4 5.3-4 5.3z"/></svg>
      <svg class="abs nav-icon" style="left:328px;top:27px" width="30" height="30" viewBox="0 0 24 24"><path fill-rule="evenodd" fill="var(--teal)" d="M10.3 2.5h3.4l.5 2.5 1.8.8 2.1-1.4 2.4 2.4-1.4 2.1.8 1.8 2.5.5v3.4l-2.5.5-.8 1.8 1.4 2.1-2.4 2.4-2.1-1.4-1.8.8-.5 2.5h-3.4l-.5-2.5-1.8-.8-2.1 1.4-2.4-2.4 1.4-2.1-.8-1.8-2.5-.5v-3.4l2.5-.5.8-1.8-1.4-2.1 2.4-2.4 2.1 1.4 1.8-.8z M12 8.8a3.2 3.2 0 1 0 0 6.4 3.2 3.2 0 0 0 0-6.4z"/></svg>
      <div class="abs home-indicator" style="top:67px"></div>
    </div>
  </section>

</div>
</body>
</html>
```